Pamphlet Days of the Family - École Sainte-Ondine

We * need a pamphlet (flyer) to describe a new project. This project is called "Family Days - École Sainte-Ondine". The text describing family days and their intended goals is attached in the downloaded .doc document. We also provided the logo (LA PRIMOVEL no font in attachment) which represents the school and those days of the family. Please write "Family Days - École Sainte-Ondine" on top of the pamphlet with the Logo in plain view (The text The days of the École Sainte-Ondine family must be associated with the logo). We need the pamphlet to be colorful, attractive and clean as much as possible. We would like to have childish drawings (see drawing example attached) and photos that represent one or both parents with their child (ren) in a SCHOOL ENVIRONMENT (very important). Parents must feel concerned. It can be a two-sided pamphlet. In color (bright colors as much as possible). The text must be in French so only FRENCH DESIGNERS ARE INVITED to work on this design because the text must remain consistent. The project can be summed up as follows: The Sainte-Ondine School wishes to open its doors so that parents can share with their child moments in their student life. They will be invited, at various times of the school year, to participate in the daily life of their child, for example ... • during special activities in class (eg reading, do-it-yourself, job presentation, etc.). events (eg, back to school, Christmas choir, carnival, etc.) • during educational and sports outings (eg skating, library, cinema, etc.) Also, they will have the opportunity to come and spend a period in their child's classroom. They will have the privilege of accompanying him during a usual learning moment. For any additional question, thank you to contact me via this page, it will be my pleasure to answer you quickly. Thank you all for your participation. * We are a committee made up of parents, teachers, school principal, school administrators. Everyone has a say in the final design. So I am only the intermediary responsible for the project. It will be my pleasure to share with you the information received from these different partners for this project.

Target Market(s)

Parents of students at a primary school (ages 5 to 12).

Font styles to use
Sans Serif

Colors

Designer to choose colors to be used in the design.

Requirements
Must have
• The Logo prominently Pamphlet Colorful (beautiful bright colors) Easy to read and understand (some parents speak very little French) Originality (Attractive) Text In French (required) and consistent
Nice to have
• One or more Childish Drawing (s) One (1) parent-child Photo (s) in a school environment Allure Épuré
Should not have
• The Dark Colors Of the Scriptures Too Small A Condensed Text Text English

```html
<!DOCTYPE html>
<html lang="fr">
<head>
<meta charset="utf-8">
<title>Les journées de la famille de Ste-Ondine</title>
<link href="https://fonts.googleapis.com/css2?family=Itim&family=Luckiest+Guy&display=swap" rel="stylesheet">
<style>
:root{
  --paper:#ffffff;
  --mist:#eeeff1;
  --sky:#1aa7e8;
  --blue:#1b7fc7;
  --red:#e8212b;
  --ink:#1b1b1b;
  --sun:#ffd400;
  --cream:#fdeeb0;
  --cloud:#e4f1fb;
  --lilac:#dcc4e3;
  --leaf:#d7e9c1;
}
*{margin:0;padding:0;box-sizing:border-box}
html,body{width:960px;height:1200px;overflow:hidden;background:#f4f1ec}
.flyer{position:relative;width:960px;height:1200px;overflow:hidden;background:linear-gradient(#fff 0,#fff 170px,var(--mist) 200px);font-family:"Itim",sans-serif;color:var(--ink)}
.abs{position:absolute}
.brand-mark{left:48px;top:30px;width:120px;height:120px;border-radius:50%;background:var(--sun)}
.brand-name{left:40px;top:156px;width:136px;text-align:center;font-size:13px;color:var(--blue)}
.title{left:192px;top:58px;font-family:"Luckiest Guy",sans-serif;font-size:30px;line-height:38px;color:var(--blue);letter-spacing:.5px}
.photo{left:640px;top:-30px;width:340px;height:340px;border-radius:50%;background:radial-gradient(circle,#d9c2ae 0,#b9c6d2 55%,var(--sun) 56%,var(--sun) 64%,#fff 65%)}
.intro{left:40px;top:208px;width:440px;font-size:15.5px;line-height:21.5px;color:var(--red)}
.invite{left:40px;top:340px;width:660px;font-size:18px;line-height:26px;color:var(--blue);font-style:italic;font-weight:bold}
.checks{left:40px;top:404px;list-style:none;font-size:15.5px;line-height:26px}
.checks li::before{content:"✓";color:var(--blue);margin-right:10px}
.more{left:40px;top:486px;width:880px;font-size:15.5px;line-height:21px;color:var(--blue)}
.band{left:0;top:543px;width:960px;height:473px}
.goal h3{font-family:"Itim",sans-serif;font-weight:normal;font-size:18px;color:var(--red);margin-bottom:4px}
.goal ul{list-style:none;font-size:15px;line-height:21px}
.goal li{padding-left:22px;position:relative}
.goal li::before{content:"✓";color:var(--red);position:absolute;left:0}
.goal--child{left:268px;top:603px;width:440px}
.goal--child h3{margin-left:110px}
.goal--school{left:36px;top:758px;width:300px}
.goal--school h3{margin-left:76px}
.goal--teacher{left:36px;top:905px;width:440px}
.goal--teacher h3{margin-left:112px}
.goal--parent{left:576px;top:800px;width:370px}
.goal--parent h3{margin-left:76px}
.node{font-size:17px;color:var(--blue);text-align:center;font-weight:bold}
.node--child{left:405px;top:752px;width:76px}
.node--school{left:297px;top:862px;width:120px;line-height:19px}
.node--parent{left:515px;top:888px;width:70px}
.hub{left:410px;top:800px;width:150px;text-align:center;font-size:16px;line-height:24px;color:#fff}
.notice{left:34px;top:1028px;width:610px;font-size:15.5px;line-height:21px;color:var(--blue)}
.watch{left:0;top:1100px;width:645px;height:100px}
.watch p{position:absolute;left:34px;top:32px;font-size:17px;line-height:22px;color:var(--red)}
.drawing{left:645px;top:1016px;width:315px;height:184px;background:linear-gradient(#fff 0,#fdf8e6 60%,#eef6e4 100%)}
</style>
</head>
<body>
<main class="flyer">
  <div class="abs photo" role="img" aria-label="Photo d'un père, d'une mère et de leurs deux enfants préparant les sacs d'école, encadrée d'un soleil jaune"></div>

  <div class="abs brand-mark" aria-hidden="true"></div>
  <div class="abs brand-name">LA PRIMOVEL</div>
  <h1 class="abs title">Les journées de la<br>famille de Ste-Ondine</h1>

  <p class="abs intro">L'école Sainte-Ondine souhaite ouvrir ses portes afin que vous puissiez partager avec votre enfant des moments de sa vie d'élève. Vous connaissez votre enfant sous plusieurs de ses facettes. Avec ce projet, vous pourrez maintenant le connaître en tant qu'élève œuvrant dans son milieu scolaire.</p>

  <p class="abs invite">Vous serez invités, à divers moments de l'année scolaire, à participer au quotidien de votre enfant, par exemple…</p>

  <ul class="abs checks">
    <li>lors d'activités spéciales en classe (ex.: lecture, bricolage, présentation de métiers, etc.)</li>
    <li>lors d'événements (ex.: la rentrée, chorale de Noël, fête foraine, etc.)</li>
    <li>lors de sorties éducatives et sportives (ex.: patinage, bibliothèque, cinéma, etc.)</li>
  </ul>

  <p class="abs more">De plus, vous aurez l'opportunité de venir passer une période dans la classe de votre enfant. Vous aurez ainsi le privilège de l'accompagner lors d'un moment d'apprentissage habituel.</p>

  <svg class="abs band" viewBox="0 0 960 473" aria-hidden="true">
    <defs>
      <marker id="tip" viewBox="0 0 10 10" refX="7" refY="5" markerWidth="7" markerHeight="7" orient="auto">
        <path d="M0,0 L10,5 L0,10 z" fill="#fff"/>
      </marker>
    </defs>
    <rect width="960" height="473" fill="var(--sky)"/>
    <g fill="var(--cloud)">
      <circle cx="300" cy="120" r="70"/><circle cx="390" cy="72" r="60"/><circle cx="480" cy="62" r="65"/><circle cx="570" cy="95" r="55"/><circle cx="650" cy="130" r="55"/>
      <rect x="235" y="110" width="480" height="82" rx="40"/>
    </g>
    <g fill="var(--lilac)">
      <circle cx="70" cy="250" r="60"/><circle cx="160" cy="205" r="68"/><circle cx="245" cy="232" r="55"/>
      <rect x="10" y="222" width="295" height="98" rx="45"/>
    </g>
    <g fill="var(--cloud)">
      <circle cx="120" cy="385" r="45"/><circle cx="230" cy="352" r="55"/><circle cx="340" cy="362" r="50"/><circle cx="430" cy="392" r="40"/>
      <rect x="40" y="368" width="460" height="96" rx="45"/>
    </g>
    <g fill="var(--leaf)">
      <circle cx="650" cy="320" r="70"/><circle cx="760" cy="282" r="80"/><circle cx="870" cy="305" r="70"/><circle cx="925" cy="375" r="55"/>
      <rect x="575" y="302" width="380" height="150" rx="60"/>
    </g>
    <g fill="none" stroke="#fff" stroke-width="2" marker-end="url(#tip)">
      <path d="M412,212 Q384,250 392,300"/>
      <path d="M478,212 Q560,236 556,322"/>
      <path d="M405,360 Q465,420 545,392"/>
    </g>
    <g fill="#fff">
      <circle cx="443" cy="219" r="34"/>
      <ellipse cx="357" cy="335" rx="62" ry="32"/>
      <circle cx="550" cy="357" r="34"/>
    </g>
  </svg>

  <div class="abs node node--child">Enfant</div>
  <div class="abs node node--school">École<br>Enseignant(e)s</div>
  <div class="abs node node--parent">Parent</div>
  <div class="abs hub">Les journées de la famille de Sainte-Ondine</div>

  <section class="abs goal goal--child">
    <h3>POUR L'ENFANT :</h3>
    <ul>
      <li>Être fier de partager un moment de sa vie scolaire, en toute simplicité, avec son parent.</li>
      <li>Développer son plein potentiel.</li>
      <li>Favoriser sa réussite éducative.</li>
    </ul>
  </section>

  <section class="abs goal goal--school">
    <h3>POUR L'ÉCOLE :</h3>
    <ul>
      <li>Vivre un projet rassembleur.</li>
      <li>Valoriser le travail de l'équipe-école.</li>
      <li>Rayonner dans sa communauté.</li>
    </ul>
  </section>

  <section class="abs goal goal--teacher">
    <h3>POUR L'ENSEIGNANT :</h3>
    <ul>
      <li>Encourager la réussite de ses élèves.</li>
      <li>Multiplier les moments privilégiés parent-enfant-enseignant dans le milieu scolaire.</li>
    </ul>
  </section>

  <section class="abs goal goal--parent">
    <h3>POUR LE PARENT :</h3>
    <ul>
      <li>Développer un sentiment d'appartenance envers l'école.</li>
      <li>Découvrir son enfant en tant qu'élève.</li>
      <li>Participer à la réussite et à la persévérance scolaire de son enfant.</li>
    </ul>
  </section>

  <p class="abs notice">Pour chaque occasion reliée au projet « Les journées de la famille de Sainte-Ondine»* vous serez informés par l'enseignant(e) de votre enfant afin que vous puissiez y participer.</p>

  <svg class="abs watch" viewBox="0 0 645 100" aria-hidden="true">
    <g fill="var(--cream)">
      <circle cx="30" cy="30" r="30"/><circle cx="110" cy="22" r="28"/><circle cx="200" cy="30" r="30"/><circle cx="300" cy="24" r="28"/><circle cx="400" cy="30" r="30"/><circle cx="500" cy="22" r="28"/><circle cx="600" cy="32" r="32"/>
      <rect x="0" y="30" width="645" height="70"/>
    </g>
  </svg>
  <div class="abs watch"><p>*Surveillez les apparitions du logo sur les communications lors des<br>Journées de la famille de Sainte-Ondine!</p></div>

  <div class="abs drawing" role="img" aria-label="Dessin d'enfant : une maison, un arbre, une famille qui se tient la main, un chien et un soleil"></div>
</main>
</body>
</html>
```